Health care technology software systems

We have a solid logo. We have company colors that will need to be used as well. We just need a great business card design. We sell to health plans but want to be modern
Updates

Need extra days to review

Target Market(s)

Health technology sector selling into Health Plans

Industry/Entity Type

Health Care Technology

Contact Information for Business Card

Name, title, address, phone number, email

Requirements
Must have
• Use of Kembrata corporate colors - Uploaded w/ our logos

```html
<!DOCTYPE html>
<html lang="en">
<head>
<meta charset="utf-8">
<title>Kembrata Business Card</title>
<link rel="stylesheet" href="https://fonts.googleapis.com/css2?family=Montserrat:wght@300;400;500;600;700&display=swap">
<style>
  :root {
    --canvas-grey: #8a8c8e;
    --charcoal: #383936;
    --royal-blue: #3a5bb0;
    --sky-blue: #00a5df;
    --leaf-green: #8cc63f;
    --wordmark-grey: #8d8e8c;
    --white: #ffffff;
  }
  * { margin: 0; padding: 0; box-sizing: border-box; }
  html, body {
    width: 1200px; height: 967px; overflow: hidden;
    background: var(--canvas-grey);
    font-family: "Montserrat", sans-serif;
  }
  .canvas { position: relative; width: 1200px; height: 967px; }

  .card { position: absolute; left: 220px; width: 756px; height: 390px; overflow: hidden; }
  .card-front { top: 50px; background: var(--charcoal); }
  .card-back { top: 474px; background: var(--sky-blue); }

  .brand {
    position: absolute; left: 0; top: 82px; width: 100%;
    display: flex; align-items: center; justify-content: center; gap: 20px;
  }
  .brand-dot {
    width: 108px; height: 108px; border-radius: 50%;
    background: var(--sky-blue); flex: none;
  }
  .brand-name {
    font-weight: 300; font-size: 46px; color: var(--wordmark-grey);
    letter-spacing: 0.01em; line-height: 1; white-space: nowrap;
  }

  .slogan-band {
    position: absolute; left: 0; top: 287px; width: 100%; height: 54px;
    background: var(--royal-blue);
    display: flex; align-items: center; justify-content: center;
  }
  .slogan {
    color: var(--white); font-size: 15px; font-weight: 400;
    letter-spacing: 0.48em; word-spacing: 0.9em;
  }

  .identity { position: absolute; left: 31px; top: 52px; color: var(--white); }
  .job-title { font-weight: 700; font-size: 29px; line-height: 1; letter-spacing: 0.01em; }
  .person-name { font-weight: 400; font-size: 29px; line-height: 1; letter-spacing: 0.08em; margin-top: 13px; }
  .name-rule { width: 205px; height: 3px; background: var(--royal-blue); margin-top: 13px; }

  .contacts { position: absolute; left: 31px; top: 193px; list-style: none; color: var(--white); }
  .contact-row {
    display: flex; align-items: center; height: 20px; margin-bottom: 19px;
    font-weight: 600; font-size: 20.5px; letter-spacing: 0.05em; white-space: nowrap;
  }
  .contact-row:nth-child(3) { margin-bottom: 15px; }
  .contact-icon { width: 22px; height: 22px; margin-right: 23px; flex: none; }

  .photo-side { position: absolute; left: 0; top: 0; width: 756px; height: 390px; }
</style>
</head>
<body>
<div class="canvas">

  <section class="card card-front">
    <div class="brand">
      <span class="brand-dot"></span>
      <span class="brand-name">Kembrata</span>
    </div>
    <div class="slogan-band"><span class="slogan">SALOGAN HERE</span></div>
  </section>

  <section class="card card-back">
    <svg class="photo-side" viewBox="0 0 756 390">
      <defs>
        <linearGradient id="pillTones" x1="0" y1="0" x2="1" y2="1">
          <stop offset="0" stop-color="#e9e4dc"/>
          <stop offset="0.35" stop-color="#5a7fd6"/>
          <stop offset="0.65" stop-color="#d9d6d3"/>
          <stop offset="1" stop-color="#4f72c9"/>
        </linearGradient>
      </defs>
      <path class="accent-arc" d="M492,0 C420,50 383,120 383,189 C383,270 430,340 517,390 L756,390 L756,0 Z" fill="var(--leaf-green)"/>
      <path class="photo-area" role="img" aria-label="Photo of assorted colourful pills and capsules"
            d="M508,0 C436,50 398,120 398,189 C398,270 446,340 535,390 L756,390 L756,0 Z" fill="url(#pillTones)"/>
    </svg>

    <div class="identity">
      <p class="job-title">TITLE HERE</p>
      <p class="person-name">YOUR NAME</p>
      <div class="name-rule"></div>
    </div>

    <ul class="contacts">
      <li class="contact-row">
        <svg class="contact-icon" viewBox="0 0 24 24"><path d="M12 2a7 7 0 0 0-7 7c0 5 7 13 7 13s7-8 7-13a7 7 0 0 0-7-7zm0 9.5a2.5 2.5 0 1 1 0-5 2.5 2.5 0 0 1 0 5z" fill="var(--white)"/></svg>
        <span>123 Dummy, Lorem Ipsum</span>
      </li>
      <li class="contact-row">
        <svg class="contact-icon" viewBox="0 0 24 24"><path d="M6.6 10.8a15 15 0 0 0 6.6 6.6l2.2-2.2a1 1 0 0 1 1-.25 11.4 11.4 0 0 0 3.6.57 1 1 0 0 1 1 1V20a1 1 0 0 1-1 1A17 17 0 0 1 3 4a1 1 0 0 1 1-1h3.5a1 1 0 0 1 1 1c0 1.25.2 2.45.57 3.57a1 1 0 0 1-.25 1z" fill="var(--white)"/></svg>
        <span>+00 1234 5XXX 9012</span>
      </li>
      <li class="contact-row">
        <svg class="contact-icon" viewBox="0 0 24 24"><path d="M1 5h22v14H1z" fill="var(--white)"/><path d="M1 5l11 8 11-8M1 19l8-7M23 19l-8-7" fill="none" stroke="var(--sky-blue)" stroke-width="1.6"/></svg>
        <span>info@email space</span>
      </li>
      <li class="contact-row">
        <svg class="contact-icon" viewBox="0 0 24 24"><path d="M6 2v18l4.5-4.2 3 6.7 2.6-1.2-3-6.6H19z" fill="var(--white)"/></svg>
        <span>www websiteaddress</span>
      </li>
    </ul>
  </section>

</div>
</body>
</html>
```